Creative & Professional Business Card for hair salon

We are looking to update our business cards. Our salon is creative, modern, progressive and professional and looking for a design that will reflect this.

```html
<!DOCTYPE html>
<html lang="en">
<head>
<meta charset="utf-8">
<title>Mind in the Mist – Business Card</title>
<link rel="stylesheet" href="https://fonts.googleapis.com/css2?family=Quicksand:wght@300&family=Old+Standard+TT&family=Oswald:wght@300&display=swap">
<style>
  :root {
    --backdrop: #c0c0c0;
    --card: #ffffff;
    --ink: #3f5a70;
    --brand: #4f7489;
    --brand-light: #6a9ab5;
    --icon-bg: #3e76a2;
    --sky-top: #1f3a72;
    --sky-mid: #5d95c8;
    --sky-low: #7cc0df;
    --sky-base: #2bbcd8;
  }
  * { margin: 0; padding: 0; box-sizing: border-box; }
  html, body { width: 1200px; height: 1200px; overflow: hidden; }
  body { background: var(--backdrop); position: relative; font-family: "Old Standard TT", serif; }

  .card {
    position: absolute;
    left: 215px;
    width: 840px;
    height: 480px;
    background: var(--card);
    box-shadow: 6px 6px 6px rgba(0,0,0,0.45);
    overflow: hidden;
  }
  .card--front { top: 58px; }
  .card--back { top: 634px; }

  .sky {
    position: absolute; inset: 0;
    background:
      radial-gradient(ellipse at 80% 55%, rgba(140,200,230,0.55), transparent 55%),
      radial-gradient(ellipse at 30% 20%, rgba(40,70,130,0.5), transparent 60%),
      linear-gradient(180deg, var(--sky-top) 0%, var(--sky-mid) 38%, var(--sky-low) 62%, var(--sky-base) 100%);
  }

  .name-panel {
    position: absolute;
    left: 0; top: 235px;
    width: 530px; height: 173px;
    background: var(--card);
  }
  .brand-name {
    position: absolute;
    right: 40px; bottom: 2px;
    font-family: "Quicksand", sans-serif;
    font-weight: 300;
    font-size: 48px;
    color: var(--brand);
    white-space: nowrap;
    display: flex; align-items: center; gap: 14px;
  }
  .brand-dot {
    width: 18px; height: 18px; border-radius: 50%;
    background: var(--brand);
  }

  .contact-band {
    position: absolute;
    left: 0; top: 101px;
    width: 301px; height: 39px;
    background: linear-gradient(90deg, #3e6fa0 0%, #5f93bd 55%, #4a82b3 100%);
  }
  .contact-band span {
    position: absolute;
    right: 16px; top: 0;
    font-family: "Oswald", sans-serif;
    font-weight: 300;
    font-size: 28px;
    line-height: 39px;
    color: #ffffff;
    letter-spacing: 0.5px;
  }

  .back-brand {
    position: absolute;
    right: 30px; top: 102px;
    font-family: "Quicksand", sans-serif;
    font-weight: 300;
    font-size: 24px;
    color: var(--brand-light);
    display: flex; align-items: center; gap: 8px;
    white-space: nowrap;
  }
  .back-brand .brand-dot { width: 10px; height: 10px; background: var(--brand-light); }

  .contact-list { list-style: none; }
  .contact-item {
    position: absolute;
    left: 46px;
    height: 43px;
    display: flex; align-items: center; gap: 25px;
    font-size: 22px;
    line-height: 32px;
    color: var(--ink);
    white-space: nowrap;
  }
  .contact-icon {
    width: 43px; height: 43px;
    background: var(--icon-bg);
    flex: none;
  }
  .contact-icon svg { width: 43px; height: 43px; display: block; }
  .item-address { top: 167px; }
  .item-web { top: 223px; }
  .item-mail { top: 279px; }
  .item-social { top: 336px; }
  .item-phone { top: 393px; }
</style>
</head>
<body>

<section class="card card--front">
  <div class="sky" role="img" aria-label="Watercolour sky with soft clouds fading from deep navy to turquoise"></div>
  <div class="name-panel">
    <div class="brand-name"><span class="brand-dot"></span>Mind in the Mist</div>
  </div>
</section>

<section class="card card--back">
  <div class="back-brand"><span class="brand-dot"></span>Mind in the Mist</div>

  <div class="contact-band"><span>CONTACT</span></div>

  <ul class="contact-list">
    <li class="contact-item item-address">
      <span class="contact-icon">
        <svg viewBox="0 0 43 43"><path d="M21.5 8c-5.5 0-9.5 4-9.5 9.2 0 6.5 9.5 17.3 9.5 17.3s9.5-10.8 9.5-17.3C31 12 27 8 21.5 8z" fill="none" stroke="#fff" stroke-width="2.4"/><circle cx="21.5" cy="17.5" r="3.6" fill="none" stroke="#fff" stroke-width="2.2"/></svg>
      </span>
      <span class="contact-text">5/27 Harbour Lane,<br>Kelmora.</span>
    </li>
    <li class="contact-item item-web">
      <span class="contact-icon">
        <svg viewBox="0 0 43 43" fill="none" stroke="#fff" stroke-width="2"><circle cx="21.5" cy="21.5" r="14"/><ellipse cx="21.5" cy="21.5" rx="6.5" ry="14"/><line x1="7.5" y1="21.5" x2="35.5" y2="21.5"/><line x1="21.5" y1="7.5" x2="21.5" y2="35.5"/><path d="M10 14h23M10 29h23"/></svg>
      </span>
      <span class="contact-text">W-www.mindinthemist.com.au</span>
    </li>
    <li class="contact-item item-mail">
      <span class="contact-icon">
        <svg viewBox="0 0 43 43" fill="none" stroke="#fff" stroke-width="2"><rect x="7" y="12" width="29" height="20"/><path d="M7 12l14.5 12L36 12M7 32l11-10M36 32L25 22"/></svg>
      </span>
      <span class="contact-text">E-salon@mindinthemist.com.au</span>
    </li>
    <li class="contact-item item-social">
      <span class="contact-icon">
        <svg viewBox="0 0 43 43"><g stroke="#fff" stroke-width="2"><line x1="14" y1="21.5" x2="29" y2="13"/><line x1="14" y1="21.5" x2="29" y2="30"/></g><g fill="#fff"><circle cx="14" cy="21.5" r="4"/><circle cx="29" cy="13" r="4"/><circle cx="29" cy="30" r="4"/></g></svg>
      </span>
      <span class="contact-text">S-www.socialpage.com.au/MindInTheMist byLiaMoreno</span>
    </li>
    <li class="contact-item item-phone">
      <span class="contact-icon">
        <svg viewBox="0 0 43 43"><path d="M12 7l6 7-3 4c2 4 6 8 10 10l4-3 7 6-4 5C22 36 7 21 7 11z" fill="#fff"/></svg>
      </span>
      <span class="contact-text">07 5310 4827</span>
    </li>
  </ul>
</section>

</body>
</html>
```